Harborline Stay Collective Business Card Design

Design a business card for Harborline Stay Collective. Look at the website for colors and reference. Card should have logo, name, title, office number, mobile number, email, URL and a tagline like, "Luxury Hotel & Resort Email Marketing" (This might change).

https://www.harborlinestaycollective.net

The rest I will leave up to your imagination.

Contact Information for Business Card

Logo, name, title, office number, mobile number, email, URL and a tagline like, "Luxury Hotel & Resort Email Marketing" (This might change).

```html
<!DOCTYPE html>
<html lang="en">
<head>
<meta charset="utf-8">
<title>Harborline Stay Collective — Business Card</title>
<link href="https://fonts.googleapis.com/css2?family=Open+Sans:wght@700;800&family=Questrial&display=swap" rel="stylesheet">
<style>
  :root {
    --backdrop: #e6e4e1;
    --card-white: #ffffff;
    --card-black: #070707;
    --accent: #ee7420;
    --ink: #111111;
    --paper-text: #f2f2f2;
    --rule: #6b6b6b;
  }
  * { margin: 0; padding: 0; box-sizing: border-box; }
  html, body {
    width: 1200px; height: 900px; overflow: hidden;
    background: var(--backdrop);
  }
  .stage {
    position: relative; width: 1200px; height: 900px;
  }
  .card {
    position: absolute; left: 310px; width: 580px; height: 332px;
    box-shadow: 0 14px 30px rgba(0,0,0,.22);
  }
  /* Front */
  .card--front {
    top: 78px; background: var(--card-white); border-radius: 26px;
    display: flex; align-items: center; justify-content: center;
  }
  .wordmark {
    display: flex; align-items: center; gap: 14px;
    font-family: "Open Sans", sans-serif; font-weight: 800;
    text-transform: uppercase; letter-spacing: .02em; line-height: 1;
  }
  .wordmark__square { width: 18px; height: 18px; background: var(--accent); flex: none; }
  .card--front .wordmark__name { font-size: 31px; color: var(--ink); }

  /* Back */
  .card--back {
    top: 490px; background: var(--card-black);
    border-radius: 0 46px 0 46px;
    font-family: "Questrial", sans-serif; color: var(--paper-text);
  }
  .person {
    position: absolute; left: 36px; top: 40px;
  }
  .person__line { display: flex; align-items: center; gap: 8px; }
  .person__name {
    font-family: "Open Sans", sans-serif; font-weight: 800;
    color: var(--accent); font-size: 19px; letter-spacing: .02em;
  }
  .person__bar { width: 2px; height: 20px; background: var(--accent); }
  .person__title { font-size: 17px; }
  .person__mobile { margin-top: 8px; font-size: 17px; gap: 10px; }

  .contacts {
    position: absolute; left: 292px; top: 120px; list-style: none;
  }
  .contacts li {
    display: flex; align-items: center; gap: 10px;
    font-size: 15.5px; height: 24px;
  }
  .contacts svg { width: 15px; height: 15px; flex: none; }
  .rule {
    position: absolute; left: 292px; right: 24px; top: 228px;
    height: 1px; background: var(--rule);
  }
  .brand-block {
    position: absolute; left: 292px; top: 246px;
  }
  .card--back .wordmark__name { font-size: 19px; color: var(--paper-text); }
  .wordmark__square--sm { width: 13px; height: 13px; }
  .tagline { margin-top: 10px; font-size: 13px; padding-left: 27px; }
</style>
</head>
<body>
<main class="stage">
  <section class="card card--front" aria-label="Card front">
    <div class="wordmark">
      <span class="wordmark__square"></span>
      <span class="wordmark__name">Harborline Stay Collective</span>
    </div>
  </section>

  <section class="card card--back" aria-label="Card back">
    <div class="person">
      <div class="person__line">
        <span class="person__name">DANIEL REYES</span>
        <span class="person__bar"></span>
        <span class="person__title">Director</span>
      </div>
      <div class="person__line person__mobile">
        <svg width="12" height="18" viewBox="0 0 12 18" aria-hidden="true"><rect x="1" y="1" width="10" height="16" rx="1.5" fill="none" stroke="var(--accent)" stroke-width="1.4"/><line x1="4.5" y1="14.5" x2="7.5" y2="14.5" stroke="var(--accent)" stroke-width="1.2"/></svg>
        <span>555.000.0000</span>
      </div>
    </div>

    <ul class="contacts">
      <li>
        <svg viewBox="0 0 16 16" aria-hidden="true"><path d="M3 1.5l2.5 0 1.2 3-1.6 1.2c.8 1.8 2.2 3.2 4 4l1.2-1.6 3 1.2v2.5c0 .8-.7 1.4-1.5 1.4C6.7 13.2 2.8 9.3 1.6 3c0-.8.6-1.5 1.4-1.5z" fill="var(--accent)"/></svg>
        <span>555.204.7300</span>
      </li>
      <li>
        <svg viewBox="0 0 16 16" aria-hidden="true"><rect x="1" y="3" width="14" height="10" fill="var(--accent)"/><path d="M1 3l7 5.5L15 3" fill="none" stroke="var(--card-black)" stroke-width="1.3"/></svg>
        <span>info@harborlinestaycollective.net</span>
      </li>
      <li>
        <svg viewBox="0 0 16 16" aria-hidden="true"><g fill="none" stroke="var(--accent)" stroke-width="1.2"><circle cx="8" cy="8" r="6.5"/><ellipse cx="8" cy="8" rx="2.8" ry="6.5"/><line x1="1.5" y1="8" x2="14.5" y2="8"/><line x1="2.5" y1="4.8" x2="13.5" y2="4.8"/><line x1="2.5" y1="11.2" x2="13.5" y2="11.2"/></g></svg>
        <span>www.harborlinestaycollective.net</span>
      </li>
      <li>
        <svg viewBox="0 0 16 16" aria-hidden="true"><path d="M8 1a4.8 4.8 0 0 1 4.8 4.8C12.8 9.5 8 15 8 15S3.2 9.5 3.2 5.8A4.8 4.8 0 0 1 8 1z" fill="var(--accent)"/><circle cx="8" cy="5.8" r="1.8" fill="var(--card-black)"/></svg>
        <span>North America</span>
      </li>
    </ul>

    <div class="rule"></div>

    <div class="brand-block">
      <div class="wordmark">
        <span class="wordmark__square wordmark__square--sm"></span>
        <span class="wordmark__name">Harborline Stay Collective</span>
      </div>
      <p class="tagline">Luxury Hotel &amp; Resort Email Marketing</p>
    </div>
  </section>
</main>
</body>
</html>
```